Webbanner-Design für Blog rund um das Thema Immobilie
Zielgruppe
Wir sind ein Blog rund um das Thema Immobilie mit Fokus auf Hausverwaltung und ergänzen unser Angebot aktuell um ein kostenpflichtiges Branchenverzeichnis. https://www.wohnobjekt-kompass.example/
Aufgabenstellung
Sofern sinnvoll, Farbgestaltung des Blogs beibehalten.
Es werden folgende Elemente in einem einheitlichen Stil benötigt:
1. Ein neues Logo für den Blog. Von Stil her gerne wie das bestehende Logo.
2. Ein Trustelement für Kunden, die im Branchenverzeichnis eingetragen sind mit Text 'Eingetragen auf Wohnobjekt-Kompass.example'
3. Werbeanzeige (jeweils: 300x250, 728x90, 300x600) mit Text 'Eintrag im Verzeichnis sichern. Sichtbar werden. Ganz einfach neue Kunden gewinnen.'
4. Werbeanzeige (jeweils: 300x250, 728x90, 300x600) mit Text 'Lassen Sie sich von neuen Kunden finden. Mit einem Eintrag in unserem Branchenverzeichnis.'
5. Werbeanzeige (jeweils: 300x250, 728x90, 300x600) mit Text 'Zielgerichtet werben? Jetzt Eintrag im Verzeichnis sichern!'
6. Werbeanzeige (jeweils: 300x250, 728x90, 300x600) mit Text 'Sie möchten von wechselwilligen Eingentümern gefunden werden? Jetzt Eintrag im Verzeichnis sichern!'
7. Werbeanzeige (jeweils: 300x250, 728x90, 300x600) mit Text 'Lassen Sie sich von Eigentümern finden. Brancheneintrag schon ab € 14,90 monatlich.'
8. Werbeanzeige (jeweils: 300x250, 728x90, 300x600) mit Text 'Die eigene Sichtbarkeit als Verwalter erhöhen? Einfach ins Branchenbuch eintragen lassen.'
9. Werbeanzeige (jeweils: 300x250, 728x90, 300x600) mit Text 'Finden Sie den passenden Anbieter für Ihre Immobilie. Schnell und kostenlos. Zum Branchenverzeichnis.'
10. Werbeanzeige (jeweils: 300x250, 728x90, 300x600) mit Text 'Das spezialisierte Branchenverzeichnis rund um die Immobilie! - 250+ Städte - 3.500+ Dienstleister - einfach suchen und finden'
11. Werbeanzeige (jeweils: 300x250, 728x90, 300x600) mit Text 'Unzufrieden mit der Hausverwaltung? Einfach eine Alternative im Verzeichnis finden!'
12. Werbeanzeige (jeweils: 300x250, 728x90, 300x600) mit Text 'Sie möchten eine Immobilie verkaufen? Finden Sie den passenden Makler in unserem Verzeichnis!'

```html
<!DOCTYPE html>
<html lang="de">
<head>
<meta charset="utf-8">
<title>Webbanner Wohnobjekt Kompass</title>
<link rel="stylesheet" href="https://fonts.googleapis.com/css2?family=Roboto:wght@400;500;700&display=swap">
<style>
  :root {
    --brand-green: #168232;
    --text-dark: #222222;
    --frame: #1a1a1a;
    --white: #ffffff;
    --wall-light: #e6e6e6;
    --wall-mid: #d6d6d6;
    --floor: #d9c2b0;
  }
  * { box-sizing: border-box; margin: 0; padding: 0; }
  html, body { width: 994px; height: 1200px; overflow: hidden; background: var(--white); }
  body { position: relative; font-family: "Roboto", sans-serif; color: var(--text-dark); }

  .ad { position: absolute; border: 1px solid var(--frame); background: var(--white); overflow: hidden; }
  .ad--rectangle { left: 358px; top: 84px; width: 253px; height: 211px; }
  .ad--leaderboard { left: 177px; top: 396px; width: 616px; height: 75px; }
  .ad--skyscraper { left: 358px; top: 573px; width: 253px; height: 507px; }

  .brand { position: absolute; color: var(--brand-green); font-weight: 400; line-height: 1.4; }
  .brand__mark { display: inline-block; width: 8px; height: 8px; background: var(--brand-green); margin-bottom: 4px; }

  .ad--rectangle .brand { left: 14px; top: 14px; font-size: 10.5px; }
  .ad--leaderboard .brand { left: 14px; top: 17px; font-size: 10.5px; }
  .ad--skyscraper .brand { left: 16px; top: 22px; font-size: 12px; }

  .room-photo {
    position: absolute;
    background: linear-gradient(180deg, var(--wall-mid) 0%, var(--wall-light) 35%, var(--wall-light) 78%, var(--floor) 88%, #cdb3a0 100%);
  }
  .ad--rectangle .room-photo { left: 0; top: 71px; right: 0; bottom: 0; }
  .ad--leaderboard .room-photo { left: 125px; top: 0; right: 0; bottom: 0; }
  .ad--skyscraper .room-photo { left: 0; top: 95px; right: 0; bottom: 0; }

  .headline { position: absolute; font-weight: 400; }
  .ad--rectangle .headline { left: 15px; top: 85px; width: 230px; font-size: 15px; line-height: 22px; }
  .ad--leaderboard .headline { left: 140px; top: 15px; font-size: 13.5px; line-height: 22px; white-space: nowrap; }
  .ad--skyscraper .headline { left: 28px; top: 170px; width: 215px; font-size: 22.5px; line-height: 30.5px; }

  .cta {
    position: absolute; width: 106px; height: 28px;
    display: flex; align-items: center; justify-content: center;
    background: var(--brand-green); color: var(--white);
    font-size: 10.5px; font-weight: 500; border-radius: 2px;
  }
  .ad--rectangle .cta { left: 132px; top: 168px; }
  .ad--leaderboard .cta { left: 488px; top: 24px; }
  .ad--skyscraper .cta { left: 28px; top: 357px; }
</style>
</head>
<body>

<section class="ad ad--rectangle" aria-label="Anzeige 300x250">
  <div class="room-photo" role="img" aria-label="Foto eines hellen, leeren Raums mit offener weißer Flügeltür und Holzdielen"></div>
  <div class="brand"><span class="brand__mark"></span><br>Wohnobjekt<br>Kompass</div>
  <p class="headline">Eintrag im Verzeichnis sichern.<br>Sichtbar werden.<br>Ganz einfach neue Kunden gewinnen.</p>
  <span class="cta">mehr erfahren</span>
</section>

<section class="ad ad--leaderboard" aria-label="Anzeige 728x90">
  <div class="room-photo" role="img" aria-label="Foto eines hellen, leeren Raums mit offenen weißen Türen und Holzdielen"></div>
  <div class="brand"><span class="brand__mark"></span><br>Wohnobjekt<br>Kompass</div>
  <p class="headline">Eintrag im Verzeichnis sichern.<br>Sichtbar werden. Ganz einfach neue Kunden gewinnen.</p>
  <span class="cta">mehr erfahren</span>
</section>

<section class="ad ad--skyscraper" aria-label="Anzeige 300x600">
  <div class="room-photo" role="img" aria-label="Foto einer offenen weißen Flügeltür in einen leeren Raum mit Holzdielen"></div>
  <div class="brand"><span class="brand__mark"></span><br>Wohnobjekt<br>Kompass</div>
  <p class="headline">Eintrag im Verzeichnis sichern. Sichtbar werden. Ganz einfach neue Kunden gewinnen.</p>
  <span class="cta">mehr erfahren</span>
</section>

</body>
</html>
```